Harbor Learning Center Posters Showing Building Blocks

We need poster designs for a School in Arizona for kids with Autism. There will be 4 such posters needed which highlight our schools building blocks. Requirements for all 4 posters are as followed: 1) We need the Harbor Learning Center Logo on each poster. I have included attachment. 2) The posters need the following titles: Building Block #1 (for the first poster), Building Block #2 for the 2nd poster, Building Block #3 for the 3rd poster, and Building Block #4 for the forth poster. 3) The main text and focus of the posters will be the following key words: For the first poster the words "Kids first in every decision". The words for the second poster are: "Students are friends with each other, and welcome new students with open arms." The words for the 3rd poster are: "The school is quiet, and students are working hard to do their best." The words for the 4th poster are: "Parents see amazing improvement in their child." 4) We would love to use some of the kids art from our schools if possible. Use your expertise to decide. I will send these out as well. 5) Try and design the posters around the key words from each poster 6) I am sure if landscape or portrait would be best so I will let the experts decide. All 4 posters need to be the same layout once decided.

Target Market(s)

These posters are for the school only. Prospective students/parents will see these posters so they will be used for Marketing from that perspective. We may put out into local community in future.

Industry/Entity Type

School

Font styles to use
Serif

Requirements
Must have
• 1) Logo (Harbor Learning Center for Growth and Discovery)
• 2) Title: as described in write up
• 3) Key words: as described in write up
Nice to have
• Kids art from school. Note: This is the first time that I have been on this site so I may have made a mistake by putting 4 posters on one project. I am assuming that I would need to pay more to have 4 posters so let me know if I need to modify the project in any way?

```html
<!DOCTYPE html>
<html lang="en">
<head>
<meta charset="utf-8">
<title>Harbor Learning Center – Building Block #2</title>
<link rel="stylesheet" href="https://fonts.googleapis.com/css2?family=Tinos:wght@400;700&family=Roboto+Condensed:wght@400&display=swap">
<style>
  :root {
    --page-bg: #e9e6e1;
    --paper-light: #f1eadf;
    --paper-dark: #ddd2bf;
    --tag-bg: #111111;
    --tag-text: #ffffff;
    --quote-red: #dd1f1f;
    --brand-ink: #2b2626;
    --brand-mark: #d8232a;
    --art-navy: #2a2f5c;
    --art-orange: #e8682a;
    --art-pink: #e0458f;
    --art-violet: #7b4fc4;
    --art-teal: #2f8f86;
  }
  * { margin: 0; padding: 0; box-sizing: border-box; }
  html, body {
    width: 1200px;
    height: 900px;
    overflow: hidden;
    background: var(--page-bg);
  }
  .poster {
    position: absolute;
    left: 295px;
    top: 30px;
    width: 610px;
    height: 840px;
    background: radial-gradient(ellipse at 50% 40%, var(--paper-light) 0%, var(--paper-light) 45%, var(--paper-dark) 100%);
    box-shadow: 0 2px 10px rgba(0,0,0,0.12);
  }
  .block-tag {
    position: absolute;
    left: 366px;
    top: 25px;
    width: 220px;
    height: 33px;
    background: var(--tag-bg);
    color: var(--tag-text);
    font-family: "Roboto Condensed", sans-serif;
    font-size: 19px;
    letter-spacing: 0.5px;
    line-height: 33px;
    text-align: center;
    word-spacing: 3px;
  }
  .kids-art {
    position: absolute;
    left: 14px;
    top: 55px;
    width: 559px;
    height: 445px;
  }
  .key-words {
    position: absolute;
    left: 0;
    top: 515px;
    width: 610px;
    text-align: center;
    font-family: "Tinos", serif;
    font-weight: 700;
    font-size: 24px;
    line-height: 28px;
    color: var(--quote-red);
    text-transform: uppercase;
  }
  .brand {
    position: absolute;
    left: 78px;
    top: 700px;
    display: flex;
    align-items: center;
    gap: 18px;
  }
  .brand-square {
    width: 46px;
    height: 46px;
    background: var(--brand-mark);
  }
  .brand-name {
    font-family: "Tinos", serif;
    font-weight: 400;
    font-size: 28px;
    line-height: 34px;
    color: var(--brand-ink);
  }
</style>
</head>
<body>
  <main class="poster">
    <div class="block-tag">BUILDING BLOCK # 2</div>

    <svg class="kids-art" viewBox="0 0 559 445" role="img" aria-label="Children's artwork from the school: colourful circles, a patterned heart and bright marbled painting">
      <defs>
        <linearGradient id="artTones" x1="0" y1="1" x2="1" y2="0">
          <stop offset="0" stop-color="var(--art-violet)"/>
          <stop offset="0.3" stop-color="var(--art-pink)"/>
          <stop offset="0.55" stop-color="var(--art-navy)"/>
          <stop offset="0.8" stop-color="var(--art-orange)"/>
          <stop offset="1" stop-color="var(--art-teal)"/>
        </linearGradient>
      </defs>
      <rect x="120" y="40" width="320" height="360" rx="40" fill="url(#artTones)" transform="rotate(-40 280 222)"/>
    </svg>

    <p class="key-words">"Students are friends with<br>each other, and welcome<br>new students with open arms."</p>

    <div class="brand">
      <div class="brand-square"></div>
      <p class="brand-name">Harbor Learning Center<br>for Growth and Discovery</p>
    </div>
  </main>
</body>
</html>
```